"HTML Email Template"

We are wanting to get a html template built for the purpose of a monthly email that we send out to our database. Currently we send them out in an email form and looking to bring some more colour and graphics to jazz it up a little.
Our webpage address is www.harborlineadvisory.com.au
It targets people in the innovation, development, strategy, collaboration and entrepreneurship space.
The monthly email contains an into paragraph and up to about ten items with links to articles etc
We would like to stick with a similar colour scheme as seen on our webpage.
The final design should look professional and edgy
Updates

Hi

We have just changed this status of this project to Guaranteed Payment
Looking forward to start receiving some great designs
Thanks

Project Deadline Extended

Target Market(s)

Senior executives in corporations, professionals

Industry/Entity Type

It Professional

```html
<!DOCTYPE html>
<html lang="en">
<head>
<meta charset="utf-8">
<title>Open Innovation: What's behind the Buzzword?</title>
<link href="https://fonts.googleapis.com/css2?family=Arimo:wght@400;700&family=Roboto:wght@300;400&display=swap" rel="stylesheet">
<style>
  :root {
    --page-bg: #eff1f4;
    --sheet-bg: #ffffff;
    --sheet-border: #a9b2bc;
    --title-blue: #2873ad;
    --brand-blue: #2e6fa8;
    --meta-grey: #8a8f99;
    --meta-strong: #6f7787;
    --body-text: #3d4147;
    --footer-bg: #b8c1c9;
    --footer-text: #ffffff;
    --header-light: #d9eefa;
    --header-mid: #8ccbee;
    --header-deep: #3a86d2;
  }
  * { box-sizing: border-box; margin: 0; padding: 0; }
  html, body { width: 1020px; height: 1200px; overflow: hidden; }
  body { background: var(--page-bg); font-family: "Arimo", Arial, sans-serif; color: var(--body-text); position: relative; }

  .newsletter {
    position: absolute; left: 149px; top: 15px; width: 722px; height: 1112px;
    background: var(--sheet-bg); border: 1px solid var(--sheet-border);
  }
  .masthead {
    position: relative; height: 95px;
    background: linear-gradient(100deg, var(--header-light) 0%, #b6e0f6 40%, var(--header-mid) 65%, var(--header-deep) 100%);
    overflow: hidden;
  }
  .masthead-swoosh { position: absolute; right: 0; top: 0; }
  .brand {
    position: absolute; left: 20px; top: 30px; display: flex; align-items: center; gap: 10px;
    font-family: "Arimo", Arial, sans-serif; font-weight: 700; font-size: 27px; color: var(--brand-blue); letter-spacing: -0.5px;
  }
  .brand-dot { width: 34px; height: 34px; border-radius: 50%; background: var(--brand-blue); }

  .article-title {
    position: absolute; left: 19px; top: 119px;
    font-family: "Roboto", Arial, sans-serif; font-weight: 300; font-size: 31px; color: var(--title-blue); letter-spacing: -0.2px;
  }
  .article-meta { position: absolute; left: 19px; top: 164px; font-size: 13px; color: var(--meta-grey); }
  .article-meta strong { color: var(--meta-strong); }

  .feature-art {
    position: absolute; left: 26px; top: 213px; width: 230px; height: 182px;
    background: radial-gradient(ellipse at 52% 45%, #c9c9f5 0%, #eeeefc 55%, #ffffff 80%);
  }
  .intro { position: absolute; left: 290px; top: 201px; width: 395px; font-size: 12.5px; line-height: 20px; }
  .read-more { display: block; margin-top: 13px; font-weight: 700; font-size: 13px; color: var(--body-text); text-decoration: none; }

  .conclusions { position: absolute; left: 40px; top: 421px; width: 645px; font-size: 12.5px; line-height: 20px; }
  .conclusions ol { margin-top: 18px; padding-left: 22px; }
  .conclusions li { margin-bottom: 10px; padding-left: 0; }

  .footer-band {
    position: absolute; left: 0; bottom: 0; width: 100%; height: 36px; background: var(--footer-bg);
    display: flex; align-items: center; justify-content: space-between; padding: 0 10px 0 34px;
  }
  .footer-tagline { color: var(--footer-text); font-weight: 700; font-size: 11.5px; }
  .social { display: flex; gap: 5px; }
  .social span { width: 24px; height: 24px; border-radius: 50%; background: #eef1f4; border: 1px solid #9aa4ad; display: block; }
</style>
</head>
<body>
  <div class="newsletter">
    <header class="masthead">
      <svg class="masthead-swoosh" width="300" height="95" viewBox="0 0 300 95" aria-hidden="true">
        <path d="M40 95 C80 40 160 10 290 0 L300 0 L300 20 C190 25 120 55 90 95 Z" fill="#1f5fae" opacity="0.55"/>
        <path d="M150 95 C190 60 240 40 300 35 L300 95 Z" fill="#2b7fd0" opacity="0.45"/>
      </svg>
      <div class="brand"><span class="brand-dot"></span>Harborline Advisory</div>
    </header>

    <h1 class="article-title">Open Innovation: What’s behind the Buzzword?</h1>
    <p class="article-meta">Posted on January 17, 2012 by <strong>Daniel Whitcombe</strong> in <strong>Innovation, Open Innovation</strong></p>

    <div class="feature-art" role="img" aria-label="Cartoon thought bubble reading Think Big above a small figure"></div>

    <div class="intro">
      <p>Innovation is higher than ever on companies' agenda. 62% of executives interviewed in a recent survey say their business strategy is "largely" or "totally" dependent on Innovation. In today's globalized competitive environment, innovation has become the key criterion by which you can assess how good a company is and how good it is likely to be in the future. To give an example of this innovation play in the emblematic mobile phone industry, Orchard Mobile, Keystone Wireless and Halo Devices, the three most…</p>
      <a class="read-more" href="https://www.harborlineadvisory.com.au">Read more…</a>
    </div>

    <section class="conclusions">
      <p>Conclusions in the report (as presented by the authors) are:</p>
      <ol>
        <li>Open Innovation is a new thing: more precisely an old practice (such as collaborating with other companies or research centers) which is being systematized and for which processes are setup at a strategic corporate level.</li>
        <li>Open Innovation has a fast pace of adoption: in less than 10 years it became it has been extremely well broadcast (especially when compared to other practices such as lean Six Sigma).</li>
        <li>It allows to tapp into an almost unlimited number if external sources.</li>
        <li>An Open Innovation strategy can take various shapes, the report proposes a matrix to position the Open Innovation strategy to implement in your company depending on your level of openness.</li>
        <li>The company implementing Open Innovation must define the right balance between depth and breadth of relationship with partners. In particular this depends on your capacity as a company to absorb external knowledge.</li>
        <li>If your company implements Open Innovation, you must (and if not you will) excel at the partner management process.</li>
        <li>Open Innovation is not Open Bar. There is no Open Innovation "free lunch". You must invest to have a return on investment.</li>
        <li>Open Innovation, is not a function, it is an attitude. It is not only about appointing a "chief open innovation officer", Open Innovation must be implemented in your company's DNA through processes, practices, tools etc.</li>
        <li>Open Innovation has not resolved the innovation's Bermuda triangle – what are the KPIs? It is hard to measure return on investment.</li>
        <li>Open Innovation Works: Shorter Time to Market, Not cheaper, higher company's innovativeness, more sustainable, better IP protection.</li>
      </ol>
    </section>

    <footer class="footer-band">
      <span class="footer-tagline">Harborline Advisory · Keeping you at the leading edge!</span>
      <div class="social" aria-label="Social links"><span></span><span></span><span></span></div>
    </footer>
  </div>
</body>
</html>
```